Easter & Summer School Dance Camps

I need two flyers one for Easter camps and one for summer school
We are a performing arts and dance academy

I want a double sided flyers one side summer school one side easter camp

Please make these flyers appeal to young dancers and performers - eye catching up to date Added Tuesday, March 1, 2016

Target Market(s)

Young children and teenagers

Industry/Entity Type

School

Font styles to use
Serif
Sans Serif

Requirements
Must have
• bright colourful

```html
<!DOCTYPE html>
<html lang="en">
<head>
<meta charset="utf-8">
<title>Once Upon a Time – Easter Workshops</title>
<link href="https://fonts.googleapis.com/css2?family=Bungee+Inline&family=Petit+Formal+Script&family=Lobster&family=Roboto:wght@300;400&display=swap" rel="stylesheet">
<style>
  :root {
    --bg-dark: #1b1418;
    --bg-warm: #5a1a1c;
    --bg-glow: #8a2a24;
    --title-red: #ec3f3a;
    --title-edge: #ffb0a8;
    --pink: #e9579c;
    --ink-light: #f3eeee;
    --ink-soft: #e6dede;
  }
  html, body { margin: 0; padding: 0; overflow: hidden; background: var(--bg-dark); }
  .flyer {
    position: relative;
    width: 849px; height: 1200px;
    overflow: hidden;
    background: var(--bg-dark);
    font-family: "Roboto", "Helvetica Neue", Arial, sans-serif;
    color: var(--ink-light);
  }
  .backdrop {
    position: absolute; inset: 0;
    background:
      radial-gradient(ellipse 420px 520px at 430px 380px, var(--bg-glow) 0%, var(--bg-warm) 45%, rgba(40,18,22,0.9) 80%, transparent 100%),
      linear-gradient(180deg, #3b1a1d 0%, #2a171b 55%, var(--bg-dark) 75%);
  }
  .title {
    position: absolute; left: 0; top: 0; margin: 0;
    font-family: "Bungee Inline", "Impact", sans-serif;
    font-weight: 400;
    font-size: 100px; line-height: 1;
    color: var(--title-red);
    -webkit-text-stroke: 2px var(--title-edge);
    text-shadow: 4px 5px 0 #7a1513, 0 0 18px rgba(255,80,70,0.35);
  }
  .title span { position: absolute; white-space: nowrap; }
  .title .l1 { left: 246px; top: 66px; }
  .title .l2 { left: 246px; top: 168px; word-spacing: 60px; }
  .title .l3 { left: 246px; top: 262px; }

  .story {
    position: absolute; left: 130px; width: 550px; top: 398px;
    text-align: center;
    font-family: "Petit Formal Script", cursive;
    font-size: 14.5px; line-height: 25px;
    color: var(--ink-light);
  }
  .story h2 { font: inherit; font-size: 15px; margin: 0; }
  .story p { margin: 0 0 28px; }
  .story .details { margin: 0; }

  .sparkle {
    position: absolute; left: 50px; top: 670px; width: 720px; height: 230px;
    background: radial-gradient(ellipse at 80% 30%, rgba(233,87,156,0.18), transparent 55%),
                radial-gradient(ellipse at 10% 80%, rgba(233,87,156,0.14), transparent 50%);
  }
  .workshop-title {
    position: absolute; left: 0; top: 0; margin: 0;
    font-family: "Lobster", cursive; font-weight: 400;
    color: var(--pink);
  }
  .workshop-title span { position: absolute; white-space: nowrap; transform: rotate(-4deg); }
  .workshop-title .w1 { left: 62px; top: 668px; font-size: 92px; }
  .workshop-title .w2 { left: 160px; top: 748px; font-size: 82px; }

  .tagline {
    position: absolute; left: 100px; width: 650px; top: 858px;
    margin: 0; text-align: center;
    font-weight: 300; font-size: 20px; line-height: 27px;
    color: var(--ink-light);
  }

  .brand {
    position: absolute; left: 44px; top: 1040px;
    display: flex; align-items: center; gap: 12px;
    font-family: "Roboto", "Helvetica Neue", Arial, sans-serif;
    font-weight: 300; font-size: 50px; color: var(--ink-light);
  }
  .brand .dot { width: 22px; height: 22px; border-radius: 50%; background: var(--ink-light); }

  .info {
    position: absolute; left: 370px; top: 978px;
    font-weight: 300; font-size: 16px; color: var(--ink-soft);
  }
  .info h3 { margin: 0 0 6px; font-weight: 300; font-size: 15px; letter-spacing: 0.2px; }
  .info ul { list-style: none; margin: 0; padding: 0; }
  .info li { margin-bottom: 22px; line-height: 20px; }
  .info li::before { content: "• "; }
</style>
</head>
<body>
<main class="flyer">
  <div class="backdrop" role="img" aria-label="Dim red brick wall glowing in stage light"></div>

  <h1 class="title">
    <span class="l1">ONCE</span>
    <span class="l2">UPON A</span>
    <span class="l3">TIME...</span>
  </h1>

  <section class="story">
    <h2>Easter Workshops</h2>
    <p>This spring, your child will enjoy a joyous journey to the magical world of Once Upon a Time for a fabulous springtime treat.</p>
    <p>We will work our magic to ensure your child enjoys every minute. Guiding each child every step of the way and inspire and encourage them to project their voices, learn energetic dance routines, catchy songs, and more importantly HAVE FUN!</p>
    <p class="details">Tuesday 5 &amp; 6 April 2016 &nbsp;|&nbsp; Age 3 – 7 years<br>10 – 12pm 18 per day or 30 for both days</p>
  </section>

  <div class="sparkle" role="img" aria-label="Scattered pink stars around the workshop heading"></div>

  <h2 class="workshop-title">
    <span class="w1">West</span>
    <span class="w2">end workshop</span>
  </h2>

  <p class="tagline">Our Easter dance camps are fun, fresh and funky,<br>mixed together<br>with a little musical theatre!</p>

  <div class="brand"><span class="dot"></span>brightstep</div>

  <section class="info">
    <h3>WEST END WORKSHOP</h3>
    <ul>
      <li>Tuesday 5 &amp; 6 April 2016 • &nbsp;8 – 16 years &nbsp;• 1-4pm</li>
      <li>30 per day/ 55 for both</li>
      <li>Venue The Meadow Hall, Elmbridge Road KT9 4XY</li>
      <li>email :hello@brightstepdance.example to book or text 07700 900123</li>
    </ul>
  </section>
</main>
</body>
</html>
```